Business Card: RW Office Partners - Your tidy answer finder

Business Name: RW Office Partners
Website: www.rwofficepartners.com.au
Email: marisol@rwofficepartners.com.au
Mobile: 61 487 902 346
Facebook: @rwofficepartners
Instrgram: @rwofficepartners

Brading Colours:
HEX
#986474
#ddccd3
#7a8498
#c9d8e4
#000000
#ffffff

Tag Line: Your organised problem solver

Link to DRAFT website:
https://helpdeskhub.sitebuilderx.com/rw-office-partners

About Page from the website:
My name is Marisol Bramwell, and I would love to assist you to become more productive in your day to day and achieve your business and personal goals.
My mission is to give you time, time to work on the important tasks of your business or to be able to spend more time with your family. I will take on the tasks you don’t have time for, don’t know well or simply don’t like to do.
I have an extensive background in Administration, Tender Coordination, Document Control, WHS and Quality Management working primarily in the Construction, Mining and Corporate World.
I am passionate about being organised, having order and making things in your life (and mine) easier! I love to watch something unfold and grow into something amazing! I am known for being the go-to problem solver, the organiser of all things, producing high standards of work even under pressure. I’m also a confident communicator, and I understand that you’re busy running your business.

Target Market(s)

Small to Medium Business who require assistance in their business by a virtual assistant.

Industry/Entity Type

Virtual Assistant

Contact Information for Business Card

Mobile: 61 487 902 346

Font styles to use
Sans Serif

Colors
ffffff

Requirements
Must have
• Branding Colours as outlined.
Contact Details as outlined.
Logo as provided.
Proper contact details - mobile, facebook, instragm, website.
Simple, Elegant, very clean looking.
Should not have
• Note cute with pictures.
Not too girly as still want to market to construction companies.

```html
<!DOCTYPE html>
<html lang="en">
<head>
<meta charset="utf-8">
<title>RW Office Partners – Business Card</title>
<link href="https://fonts.googleapis.com/css2?family=Lato:wght@400;700&display=swap" rel="stylesheet">
<style>
  :root {
    --page-bg: #e6e1dc;
    --card-light: #efeae7;
    --brand-maroon: #986474;
    --brand-slate: #5f6d7c;
    --text-on-maroon: #eadcdc;
    --text-soft: #e3d2d5;
    --logo-colour: #986474;
  }
  html, body {
    margin: 0;
    padding: 0;
    width: 1200px;
    height: 1047px;
    overflow: hidden;
    background: var(--page-bg);
    font-family: "Lato", sans-serif;
  }
  .business-card {
    position: absolute;
    left: 120px;
    top: 261px;
    width: 960px;
    height: 524px;
    border-radius: 24px;
    overflow: hidden;
    background: var(--card-light);
    box-shadow: 0 10px 30px rgba(60, 40, 45, 0.18);
  }
  .card-shapes {
    position: absolute;
    inset: 0;
  }
  .contact-side {
    position: absolute;
    left: 44px;
    top: 0;
    color: var(--text-on-maroon);
  }
  .person-name {
    position: absolute;
    top: 88px;
    margin: 0;
    font-size: 35px;
    font-weight: 700;
    letter-spacing: 0.5px;
    white-space: nowrap;
  }
  .person-role {
    position: absolute;
    top: 140px;
    margin: 0;
    font-size: 22px;
    font-weight: 400;
    color: var(--text-soft);
    white-space: nowrap;
  }
  .divider {
    position: absolute;
    width: 38px;
    height: 2px;
    background: var(--text-soft);
    opacity: 0.8;
  }
  .divider--top { top: 197px; }
  .divider--bottom { top: 362px; }
  .detail-row {
    position: absolute;
    display: flex;
    align-items: center;
    gap: 18px;
    font-size: 21px;
    white-space: nowrap;
    color: var(--text-on-maroon);
  }
  .detail-icon {
    width: 22px;
    height: 22px;
    flex: none;
  }
  .detail-row--phone { top: 236px; }
  .detail-row--email { top: 266px; }
  .detail-row--web { top: 295px; }
  .detail-row--social-a { top: 392px; }
  .detail-row--social-b { top: 424px; }
  .brand-mark {
    position: absolute;
    left: 560px;
    width: 400px;
    top: 236px;
    text-align: center;
    font-size: 38px;
    font-weight: 700;
    color: var(--logo-colour);
    white-space: nowrap;
  }
</style>
</head>
<body>
  <div class="business-card">
    <svg class="card-shapes" width="960" height="524" viewBox="0 0 960 524" aria-hidden="true">
      <path class="maroon-panel" d="M0 0 H557 Q400 262 532 524 H0 Z" fill="var(--brand-maroon)"/>
      <path class="slate-edge" d="M557 0 Q414 262 558 524 H532 Q400 262 557 0 Z" fill="var(--brand-slate)"/>
    </svg>

    <div class="contact-side">
      <h1 class="person-name">JOHN SMITH</h1>
      <p class="person-role">Founder &amp; CEO</p>
      <div class="divider divider--top"></div>

      <div class="detail-row detail-row--phone">
        <svg class="detail-icon" viewBox="0 0 24 24" aria-hidden="true">
          <path d="M6.6 3.5 9 6.5 7.6 8.8c1 2.4 3.2 4.6 5.6 5.6l2.3-1.4 3 2.4-1.6 3.1C10.5 18.3 5.7 13.5 3.5 7.1z" fill="none" stroke="currentColor" stroke-width="1.8" stroke-linejoin="round"/>
        </svg>
        <span>61 487 902 346</span>
      </div>
      <div class="detail-row detail-row--email">
        <svg class="detail-icon" viewBox="0 0 24 24" aria-hidden="true">
          <rect x="3" y="6" width="18" height="12" fill="currentColor"/>
          <path d="M3 6 12 13 21 6" fill="none" stroke="#986474" stroke-width="1.6"/>
        </svg>
        <span>marisol@rwofficepartners.com.au</span>
      </div>
      <div class="detail-row detail-row--web">
        <svg class="detail-icon" viewBox="0 0 24 24" aria-hidden="true">
          <g fill="none" stroke="currentColor" stroke-width="1.6">
            <circle cx="12" cy="12" r="8.5"/>
            <ellipse cx="12" cy="12" rx="3.8" ry="8.5"/>
            <path d="M3.5 12h17M5 7.5h14M5 16.5h14"/>
          </g>
        </svg>
        <span>www.rwofficepartners.com.au</span>
      </div>

      <div class="divider divider--bottom"></div>

      <div class="detail-row detail-row--social-a">
        <svg class="detail-icon" viewBox="0 0 24 24" aria-hidden="true">
          <circle cx="12" cy="12" r="9" fill="none" stroke="currentColor" stroke-width="1.6"/>
        </svg>
        <span>@rwofficepartners</span>
      </div>
      <div class="detail-row detail-row--social-b">
        <svg class="detail-icon" viewBox="0 0 24 24" aria-hidden="true">
          <circle cx="12" cy="12" r="9" fill="none" stroke="currentColor" stroke-width="1.6"/>
        </svg>
        <span>@rwofficepartners</span>
      </div>
    </div>

    <div class="brand-mark">RW Office Partners</div>
  </div>
</body>
</html>
```